Website for software company "velbra"

We need a website for our software company/startup named "velbra". We are developing several products (currently 3 standard-software products) which are all in different sectors, but all our products are available for Laptops/PC/Mobile Phones/Tablets, ... We do also create custom software and support our customers with consulting to optimize their processes.
We already have a Logo which you can find in the attached files.
We are a young team of 4 members (two founders and 2 employees).

To get an idea of our products -> the first one is a planning software for healthcare organizations (eg. Mercyway, firebrigade, pharmacy), the second one is a booking software for sport clubs and the third one is a competition software for sports hunting. You see very diverse. Include or ignore this info of our products as you like.

The design has to be a bootstrap 4 (or higher) design. We have licenced FontAwesome as iconset. Responsive design should come without saying.

Coding

Coded - Design and coding required

Number of Pages Required

5+ page

Font styles to use
Sans Serif

Requirements
Must have
• Starting page, product pages, news section, contact, team, services

```html
<!DOCTYPE html>
<html lang="en">
<head>
<meta charset="utf-8">
<title>velbra – Software consulting and development</title>
<link rel="stylesheet" href="https://fonts.googleapis.com/css2?family=IBM+Plex+Sans:wght@300;400;500;600;700&display=swap">
<style>
:root{
  --orange:#f58220;
  --navy:#1d2733;
  --gray:#ebebeb;
  --text:#3a3f47;
  --muted:#6b7079;
  --white:#ffffff;
}
*{box-sizing:border-box;margin:0;padding:0}
html,body{width:1200px;height:3663px;overflow:hidden}
body{position:relative;background:var(--white);font-family:"IBM Plex Sans",Arial,sans-serif;color:var(--text)}
.backdrop{position:absolute;left:0;top:0;width:1200px;height:3663px;z-index:0}
section,header,footer{position:absolute;left:0;width:1200px;z-index:1}
.btn{display:inline-block;font-size:11px;font-weight:500;padding:7px 18px;color:var(--white);border-radius:1px;border-bottom:3px solid rgba(0,0,0,.15)}
.btn-orange{background:var(--orange)}
.btn-navy{background:var(--navy)}
.accent{color:var(--orange);font-weight:500}
.section-title{font-size:26px;font-weight:400;color:var(--navy);text-align:center}

/* header */
.site-header{top:0;height:62px;background:var(--white)}
.brand{position:absolute;left:200px;top:16px;display:flex;align-items:center;gap:8px;font-size:28px;font-weight:600;color:var(--navy);letter-spacing:.5px}
.brand .mark{width:18px;height:18px;background:var(--orange)}
.main-nav{position:absolute;right:200px;top:19px;display:flex;align-items:center;gap:30px;font-size:11px;font-weight:500;color:var(--navy)}
.main-nav .active{color:var(--orange)}
.main-nav .login{background:var(--navy);color:var(--white);padding:7px 14px}

/* hero */
.hero-photo{top:62px;height:580px;background:linear-gradient(120deg,#2d3f52 0%,#6c7f94 35%,#b9c3cc 55%,#4f6780 75%,#22344a 100%);clip-path:polygon(0 0,100% 0,100% 88.6%,0 58.3%)}
.hero-copy{position:absolute;left:200px;top:150px;width:520px}
.hero-copy h1{font-size:35px;font-weight:400;line-height:1.28;color:var(--white)}
.hero-copy h1 b{font-weight:500}
.hero-copy .btn{margin-top:22px}

/* welcome */
.welcome{top:600px;text-align:center}
.welcome h2{font-size:29px;font-weight:400;color:var(--navy)}
.welcome h2 span{font-weight:600;color:var(--navy)}
.welcome p{width:660px;margin:28px auto 0;font-size:10.5px;line-height:1.8;color:var(--text)}
.welcome .btn{margin-top:30px}

/* products */
.products{top:930px}
.product-grid{position:absolute;left:200px;top:115px;width:800px;display:flex;justify-content:space-between}
.product-card{position:relative;width:250px;height:190px;background:var(--white);box-shadow:0 2px 8px rgba(0,0,0,.08);text-align:center;padding-top:36px}
.product-card .corner{position:absolute;left:0;top:-55px}
.product-card h3{font-size:14px;font-weight:500;color:var(--navy)}
.product-card p{font-size:10px;line-height:1.55;color:var(--muted);width:200px;margin:12px auto 0}
.product-card .btn{margin-top:16px;padding:6px 18px}

/* services */
.services{top:1440px}
.services h2{position:absolute;left:200px;top:0;font-size:27px;font-weight:400;color:var(--navy)}
.services h2 b{font-weight:600}
.service-list{position:absolute;top:50px;list-style:none;font-size:13px;font-weight:500;color:var(--navy)}
.service-list li{height:30px;padding-left:22px;position:relative}
.service-list li::before{content:"";position:absolute;left:2px;top:4px;border-left:6px solid var(--navy);border-top:4px solid transparent;border-bottom:4px solid transparent}
.services .btn{position:absolute;left:200px;top:200px}
.service-photos{position:absolute;left:628px;top:6px;width:373px;height:298px;display:flex;gap:14px}
.service-photo{flex:1;height:100%}

/* team */
.team{top:1798px;left:95px;width:1012px;height:450px;background:var(--white);box-shadow:0 2px 10px rgba(0,0,0,.08);border-bottom:3px solid var(--orange)}
.team .section-title{margin-top:58px}
.team-grid{display:flex;justify-content:center;gap:45px;margin-top:22px}
.member{width:162px;text-align:center}
.member .portrait{width:162px;height:162px;border-radius:50%;border:3px solid var(--orange);border-top-color:var(--navy);background:linear-gradient(160deg,#e1e5ea,#8d9aa8)}
.member h4{margin-top:20px;font-size:12px;font-weight:600;color:var(--navy)}
.member span{font-size:10px;color:var(--orange)}
.team .center{text-align:center;margin-top:34px}

/* technology */
.technology{top:2310px}
.technology h2{position:absolute;left:200px;top:46px;font-size:27px;font-weight:400;color:var(--navy)}
.technology p{position:absolute;left:200px;top:108px;width:390px;font-size:27px;font-weight:300;line-height:1.32;color:var(--navy)}
.tech-arrows{position:absolute;left:200px;top:238px}
.tech-tile{position:absolute;width:158px;height:145px;background:var(--white);display:flex;flex-direction:column;align-items:center;justify-content:center;gap:8px;font-size:24px;color:var(--navy);box-shadow:0 1px 4px rgba(0,0,0,.06)}
.tech-tile .dot{width:34px;height:34px;border-radius:50%}

/* news */
.news{top:2786px}
.news-grid{position:absolute;left:200px;top:60px;width:800px;display:flex;justify-content:space-between}
.news-card{width:250px;height:285px;background:var(--white);box-shadow:0 2px 8px rgba(0,0,0,.08);border-bottom:3px solid var(--orange)}
.news-card .thumb{height:155px}
.news-card .body{padding:26px 25px 0}
.news-card time{font-size:9px;font-weight:600;color:var(--orange)}
.news-card h3{margin-top:8px;font-size:12px;font-weight:500;line-height:1.5;color:var(--navy)}
.news-card .more{margin-top:20px;font-size:10px;color:var(--orange);display:flex;align-items:center;gap:14px}
.news .center{position:absolute;top:378px;width:1200px;text-align:center}

/* footer */
.site-footer{top:3200px;height:463px}
.footer-brand{position:absolute;left:200px;top:110px;display:flex;align-items:center;gap:8px;font-size:36px;font-weight:600;color:var(--white)}
.footer-brand .mark{width:22px;height:22px;background:var(--orange)}
.contact-info{position:absolute;left:200px;top:170px;color:var(--white)}
.contact-info .call{font-size:18px}
.contact-info .call b{color:var(--orange);font-weight:400}
.contact-info .mail{margin-top:12px;font-size:10px}
.contact-info .mail b{color:var(--orange);font-weight:400}
.contact-info .addr{margin-top:14px;font-size:9.5px;line-height:1.55}
.contact-info .addr b{color:var(--orange);font-weight:600}
.quick-links{position:absolute;left:527px;top:150px;color:var(--white)}
.quick-links h4{font-size:11px;font-weight:600;color:var(--orange)}
.quick-links ul{list-style:none;margin-top:18px;font-size:9.5px}
.quick-links li{height:23px}
.follow{position:absolute;left:0;top:319px;width:612px;height:70px;background:var(--orange);display:flex;align-items:center;gap:8px;padding-left:200px;color:var(--navy);font-size:11px;font-weight:500}
.follow .social{width:28px;height:28px;border-radius:50%;background:var(--navy)}
.follow .social.lit{background:var(--white)}
.follow span{margin-right:8px}
.quote-form{position:absolute;left:776px;top:83px;width:225px;height:305px;background:#e6e6e6;padding:22px 22px 0;text-align:center}
.quote-form small{display:block;font-size:10px;font-weight:600;color:var(--navy)}
.quote-form h4{font-size:15px;font-weight:500;color:var(--orange);margin-top:4px}
.field{background:var(--white);border:1px solid #cfd2d6;height:28px;font-size:8.5px;color:var(--muted);text-align:left;padding:9px 12px}
.row{display:flex;gap:6px;margin-top:16px}
.row .field{flex:1}
.quote-form .field.full{margin-top:8px}
.quote-form .field.msg{height:72px}
.quote-form .btn{margin-top:22px;padding:7px 36px}
.copyright{position:absolute;left:200px;top:426px;font-size:9px;color:#c9ced4}
.copyright b{color:var(--orange);font-weight:500}
</style>
</head>
<body>

<svg class="backdrop" viewBox="0 0 1200 3663" aria-hidden="true">
  <polygon points="0,758 1200,1000 1200,2840 0,2600" fill="#ebebeb"/>
  <polygon points="0,1260 1200,1392 1200,2018 0,1785" fill="#f58220"/>
  <polygon points="800,515 1200,574 1200,640" fill="#1d2733"/>
  <polygon points="0,3200 1200,3321 1200,3663 0,3663" fill="#1d2733"/>
</svg>

<header class="site-header">
  <div class="brand"><span class="mark"></span>velbra</div>
  <nav class="main-nav">
    <span class="active">Home</span><span>Product</span><span>Services</span><span>Team</span><span>News</span><span>Contact Us</span>
    <span class="login">&#9679; Login / Sign Up</span>
  </nav>
</header>

<section class="hero-photo" role="img" aria-label="Photo of a young team working together at computers in a bright office"></section>
<section style="top:0;height:0">
  <div class="hero-copy">
    <h1>Software consulting and <b>development</b> for your <b>digital success</b></h1>
    <span class="btn btn-orange">Contact Us</span>
  </div>
</section>

<section class="welcome">
  <h2>Welcome to <span>velbra</span></h2>
  <p>Lorem Ipsum is simply dummy text of the printing and typesetting industry. Lorem Ipsum has been the industry's standard dummy text ever since the 1500s, when an unknown printer took a galley of type and scrambled it to make a type specimen book. It has survived not only five centuries, but also the leap into electronic typesetting, remaining essentially unchanged. It was popularised in the 1960s with the release of Letterfold sheets containing Lorem Ipsum passages, and more recently with desktop publishing software like Pagecraft including versions of Lorem Ipsum.</p>
  <span class="btn btn-orange">Our Team</span>
</section>

<section class="products">
  <h2 class="section-title">Our <span class="accent">Products</span></h2>
  <div class="product-grid">
    <article class="product-card">
      <svg class="corner" width="78" height="112" viewBox="0 0 78 112"><polygon points="0,0 78,56 0,112" fill="#1d2733"/><g fill="none" stroke="#f58220" stroke-width="3"><rect x="10" y="40" width="24" height="22"/><line x1="10" y1="48" x2="34" y2="48"/><line x1="16" y1="36" x2="16" y2="42"/><line x1="28" y1="36" x2="28" y2="42"/></g></svg>
      <h3>Planning Software</h3>
      <p>Lorem Ipsum is simply dummy text of the printing and typesetting industry lorem Ipsum has been the industry.</p>
      <span class="btn btn-navy">Read More</span>
    </article>
    <article class="product-card">
      <svg class="corner" width="78" height="112" viewBox="0 0 78 112"><polygon points="0,0 78,56 0,112" fill="#f58220"/><g fill="none" stroke="#fff" stroke-width="3"><rect x="10" y="40" width="24" height="20" rx="2"/><polyline points="15,50 20,55 29,45"/></g></svg>
      <h3>Booking Software</h3>
      <p>Lorem Ipsum is simply dummy text of the printing and typesetting industry lorem Ipsum has been the industry.</p>
      <span class="btn btn-orange">Read More</span>
    </article>
    <article class="product-card">
      <svg class="corner" width="78" height="112" viewBox="0 0 78 112"><polygon points="0,0 78,56 0,112" fill="#1d2733"/><g fill="none" stroke="#f58220" stroke-width="3"><path d="M12 40 h20 v8 a10 10 0 0 1 -20 0z"/><line x1="22" y1="58" x2="22" y2="64"/><line x1="15" y1="65" x2="29" y2="65"/></g></svg>
      <h3>Competition Software</h3>
      <p>Lorem Ipsum is simply dummy text of the printing and typesetting industry lorem Ipsum has been the industry.</p>
      <span class="btn btn-navy">Read More</span>
    </article>
  </div>
</section>

<section class="services">
  <h2>Our <b>Services</b></h2>
  <ul class="service-list" style="left:200px">
    <li>Software Development</li><li>Testing &amp; QA</li><li>Application Services</li><li>UX/UI Design</li><li>IT Consulting</li>
  </ul>
  <ul class="service-list" style="left:425px">
    <li>Data Analytics</li><li>Help Desk Services</li><li>Infrastructure</li><li>Cybersecurity</li>
  </ul>
  <span class="btn btn-navy">Contact Us</span>
  <div class="service-photos">
    <div class="service-photo" style="background:linear-gradient(160deg,#f3efe9,#d9d2c8)" role="img" aria-label="Photo of pencils in a cup on a desk"></div>
    <div class="service-photo" style="background:linear-gradient(160deg,#c9d7e6,#7d93a9)" role="img" aria-label="Photo of hands working on a tablet and laptop"></div>
    <div class="service-photo" style="background:linear-gradient(160deg,#f4f4f4,#d7dbe0)" role="img" aria-label="Photo of a person writing notes"></div>
  </div>
</section>

<section class="team">
  <h2 class="section-title">Our <span class="accent">Talented Teams</span></h2>
  <div class="team-grid">
    <div class="member"><div class="portrait" role="img" aria-label="Portrait photo of a founder"></div><h4>Standard Chunk</h4><span>Founders</span></div>
    <div class="member"><div class="portrait" role="img" aria-label="Portrait photo of a founder"></div><h4>Standard Chunk</h4><span>Founders</span></div>
    <div class="member"><div class="portrait" role="img" aria-label="Portrait photo of an employee"></div><h4>Standard Chunk</h4><span>Employees</span></div>
    <div class="member"><div class="portrait" role="img" aria-label="Portrait photo of an employee"></div><h4>Standard Chunk</h4><span>Employees</span></div>
  </div>
  <div class="center"><span class="btn btn-navy">Explore More</span></div>
</section>

<section class="technology">
  <h2>Our <span class="accent">Technology</span></h2>
  <p>Lorem Ipsum is simply dummy text of the printing typesetting industry.</p>
  <svg class="tech-arrows" width="60" height="46" viewBox="0 0 60 46"><polygon points="22,2 2,23 22,44" fill="#1d2733"/><polygon points="30,2 50,23 30,44" fill="#f58220"/></svg>
  <div class="tech-tile" style="left:684px;top:0"><span class="dot" style="background:#1d2733"></span>Dotframe</div>
  <div class="tech-tile" style="left:843px;top:22px"><span class="dot" style="background:#f58220"></span>Kavra</div>
  <div class="tech-tile" style="left:684px;top:146px"><span class="dot" style="background:#3d4a57"></span>Nodel</div>
  <div class="tech-tile" style="left:843px;top:168px"><span class="dot" style="background:#6b7c8d"></span>Serpy</div>
</section>

<section class="news">
  <h2 class="section-title">Latest <span class="accent">News</span></h2>
  <div class="news-grid">
    <article class="news-card"><div class="thumb" role="img" aria-label="Photo of a person holding a phone and coffee" style="background:linear-gradient(135deg,#8fb3c6,#e4ddd3)"></div><div class="body"><time>MARCH-12-2022</time><h3>There are many variations lorem Ipsum available, literature</h3><div class="more">Read More <span>&#8250;</span></div></div></article>
    <article class="news-card"><div class="thumb" role="img" aria-label="Photo of hands typing on a laptop" style="background:linear-gradient(135deg,#dfe3e7,#8a97a3)"></div><div class="body"><time>MARCH-12-2022</time><h3>There are many variations lorem Ipsum available, literature</h3><div class="more">Read More <span>&#8250;</span></div></div></article>
    <article class="news-card"><div class="thumb" role="img" aria-label="Photo of colleagues meeting in an office" style="background:linear-gradient(135deg,#c8ced4,#4b5a68)"></div><div class="body"><time>MARCH-12-2022</time><h3>There are many variations lorem Ipsum available, literature</h3><div class="more">Read More <span>&#8250;</span></div></div></article>
  </div>
  <div class="center"><span class="btn btn-navy">View All</span></div>
</section>

<footer class="site-footer">
  <div class="footer-brand"><span class="mark"></span>velbra</div>
  <div class="contact-info">
    <div class="call"><b>Call.</b> 123-456-7890</div>
    <div class="mail"><b>E.</b> info@velbra.com</div>
    <div class="addr"><b>VELBRA</b><br>4111 Harlow Lorem Ipsum Site Location,<br>Dummy Design - MS 39180</div>
  </div>
  <div class="quick-links">
    <h4>Quick Links</h4>
    <ul><li>Home</li><li>Product</li><li>Services</li><li>Team</li><li>News</li><li>Contact Us</li></ul>
  </div>
  <div class="follow"><span>Follow Us</span><i class="social"></i><i class="social lit"></i><i class="social"></i><i class="social"></i></div>
  <form class="quote-form">
    <small>Need Help?</small>
    <h4>Get A Free Quote Today!</h4>
    <div class="row"><div class="field">Name</div><div class="field">Phone</div></div>
    <div class="field full">Email</div>
    <div class="field full msg">Message...</div>
    <span class="btn btn-orange">Send</span>
  </form>
  <div class="copyright">©2022 <b>VELBRA</b> • All Rights Reserved</div>
</footer>

</body>
</html>
```